依頼詳細
PCとスマホデザインの両方納品をいただきますが、
まずはデザインイメージが確認しやすいPCページのみの提案をお願いします。
スマホページは当選者に納品時にお願いしたいと思います。
スマホサイズは横幅750pxのサイズで作成してください。
(Lumexaディスプレイに対応するため)
レスポンシブウェブデザインを意識したデザインでお願いします。

■サイトマップ
添付の画面遷移図をご確認ください。

■参考サイト
https://kelparoute.com/
https://mivolune.jp/sportsevent/

■内容について
建築工務店が開催するイベント情報を掲載・告知をするサイトになります。
開催するイベント内容は添付のチラシのような内容の予定です。

■素材写真
画像データについては、フリー素材から流用して
イメージ画像に当て込んでください。
足りない場合は、一旦他のサイトの写真をサンプルとして
入れてください。(サンプルなどの表記をお願いします)
また、購入が必要な写真などを利用した場合、
価格とサイト名を教えてください。

また、Velmora Stockで定期契約をしていますので、
Velmora Stockの画像は使用できます。
デザイン時はカンプ画像をお入れいただきますようお願いします。

■ワイヤーフレーム
https://wire.pelvrin.com/view/a7392cdd-1148-4f0b-9d3e-e84521b07f3a-d318/
コンテンツの構成としてワイヤーフレームを作成しましたが
必ずしもワイヤーフレームの通りではなくて大丈夫です。
TOPページに配置するコンテンツを見ていただき、デザインは
デザイナーの皆様におまかせしたいと思います。

----------------------------------------------------------------------------
【制作物に対するお願い】

■サイズについて
TOPデザイン自体のアートボードサイズは、
横幅1366px、コンテンツ幅は1000pxでお願いします。
(縦幅の制限はございません)

■フォントについて
・無料で使えるフォントで作成をお願いします。
・OSに紐づくフォントの使用は控えていただければと思います (ヒラギノなど)

サイトURL
ページ数
1ページ
希望イメージ
シンプル 複雑
単色 カラフル
暗い 明るい
日常 高級
遊び心 厳粛
未来的 伝統的
女性的 男性的
希望する色
ベースカラー:白、緑 ポイントカラー:オレンジ
納品ファイル
• イラストレーター形式 (.ai)
• フォトショップ形式 (.psd)
補足説明
上記のいずれか1つ(アウトラインありとなしの2つ)と高解像度JPGを納品お願いします。
ロゴデータを追加で添付しました。

```html
<!DOCTYPE html>
<html lang="ja">
<head>
<meta charset="utf-8">
<title>森野工務店 EVENT &amp; INFORMATION</title>
<link href="https://fonts.googleapis.com/css2?family=Dela+Gothic+One&family=Noto+Sans+JP:wght@400;500;700&display=swap" rel="stylesheet">
<style>
:root{
  --green:#3f8f2c;
  --green-dark:#2f6f1f;
  --green-light:#5aa63c;
  --orange:#f28a1a;
  --orange-dark:#e0750a;
  --ink:#222;
  --muted:#777;
  --line:#e2e2e2;
  --gray-bg:#f4f4f2;
  --white:#fff;
}
*{box-sizing:border-box;margin:0;padding:0}
html,body{width:1200px;height:3548px;overflow:hidden}
body{font-family:"Noto Sans JP",sans-serif;color:var(--ink);background:var(--white);position:relative}
.display{font-family:"Dela Gothic One","Noto Sans JP",sans-serif}

/* hero */
.hero{position:absolute;left:0;top:0;width:1200px;height:390px;
  background:linear-gradient(90deg,var(--green-dark) 0%,var(--green) 50%,var(--green-light) 100%);
  clip-path:polygon(0 0,100% 0,100% 290px,50% 390px,0 290px)}
.hero-city{position:absolute;left:360px;top:200px;width:480px;height:150px;background:rgba(255,255,255,.12)}
.hero-art-left{position:absolute;left:60px;top:110px;width:200px;height:200px;background:rgba(255,255,255,.18);border-radius:8px}
.hero-art-right{position:absolute;left:900px;top:160px;width:220px;height:160px;background:rgba(255,255,255,.18);border-radius:8px}
.brand{position:absolute;left:16px;top:16px;display:flex;align-items:center;gap:10px;color:var(--white);font-weight:700;font-size:18px}
.brand-mark{width:22px;height:22px;background:var(--white)}
.hero-title{position:absolute;left:0;top:172px;width:1200px;text-align:center;color:var(--white);font-size:58px;letter-spacing:4px}
.hero-rule{position:absolute;left:410px;top:258px;width:380px;height:3px;background:var(--white)}
.hero-sub{position:absolute;left:0;top:276px;width:1200px;text-align:center;color:var(--white);font-weight:700;font-size:18px;letter-spacing:3px}
.social{position:absolute;left:928px;top:0;width:160px;height:40px;background:#111;display:flex;justify-content:center;align-items:center;gap:22px}
.social span{width:14px;height:14px;border:2px solid var(--white);border-radius:3px}
.apply-tab{position:absolute;left:1088px;top:0;width:112px;height:120px;background:var(--orange);color:var(--white);text-align:center;padding-top:26px}
.apply-tab svg{display:block;margin:0 auto 8px}
.apply-tab b{font-family:"Dela Gothic One",sans-serif;font-weight:400;font-size:16px;display:block}
.apply-tab small{font-size:11px}

/* section heads */
.label{display:inline-block;background:#111;color:var(--white);font-size:26px;padding:2px 8px;line-height:1.1;letter-spacing:2px}
.label.green{background:var(--green)}
.label-ja{font-size:14px;font-weight:700;margin-top:8px}
.center{text-align:center}

/* events */
.events-head{position:absolute;left:0;top:586px;width:1200px}
.event-card{position:absolute;left:160px;width:880px;height:220px;border-bottom:1px solid var(--line);display:flex;align-items:center}
.event-photo{width:260px;height:160px;margin-left:20px;flex:none}
.event-body{margin-left:36px;flex:1}
.event-title{font-size:18px;font-weight:700;margin-bottom:18px}
.event-row{display:flex;font-size:12px;color:var(--muted);margin-bottom:10px}
.event-row i{width:12px;height:12px;border:1px solid #aaa;border-radius:50%;margin-right:8px;margin-top:2px}
.event-row em{font-style:normal;width:86px}
.event-row span{color:var(--ink)}
.event-apply{width:64px;height:64px;background:var(--orange);color:var(--white);text-align:center;margin-right:28px;padding-top:14px;border-radius:4px}
.event-apply b{font-family:"Dela Gothic One",sans-serif;font-weight:400;font-size:15px;display:block}
.event-apply small{font-size:10px}
.btn{display:flex;align-items:center;justify-content:center;border-radius:40px;background:var(--green-dark);color:var(--white);font-family:"Dela Gothic One",sans-serif;font-size:16px;letter-spacing:1px}
.btn-more{position:absolute;left:480px;top:1560px;width:240px;height:64px}

/* news */
.news{position:absolute;left:0;top:1740px;width:1200px;height:540px;background:var(--gray-bg)}
.news-head{position:absolute;left:160px;top:120px}
.news-more{position:absolute;left:160px;top:288px;width:180px;height:50px}
.news-list{position:absolute;left:440px;top:150px;width:600px;list-style:none}
.news-list li{display:flex;height:76px;align-items:center;border-bottom:1px solid #dcdcd8;font-size:14px}
.news-list time{width:150px;color:var(--muted);font-size:12px}

/* access */
.access-head{position:absolute;left:160px;top:2364px}
.access-addr{position:absolute;left:800px;top:2380px;font-size:12px;line-height:1.9;color:#444}
.map{position:absolute;left:160px;top:2468px;width:880px;height:324px;background:linear-gradient(135deg,#eef0ec,#e2e7e0)}
.map-pin{position:absolute;left:556px;top:2540px;background:var(--white);border:1px solid #ccc;padding:4px 10px;font-size:12px;color:#c33}

/* apply */
.apply{position:absolute;left:0;top:2900px;width:1200px;height:500px;background:var(--orange);
  clip-path:polygon(0 0,50% 100px,100% 0,100% 100%,0 100%)}
.apply-head{position:absolute;left:0;top:3030px;width:1200px}
.apply-head .label{background:#111}
.apply-head .label-ja{color:var(--white)}
.apply-text{position:absolute;left:0;top:3130px;width:1200px;text-align:center;color:var(--white);font-size:13px}
.apply-btn{position:absolute;left:400px;top:3196px;width:400px;height:66px;background:var(--white);color:var(--orange);border-radius:40px;display:flex;align-items:center;justify-content:center;gap:10px;font-family:"Dela Gothic One",sans-serif;font-size:20px}
.apply-btn small{font-family:"Noto Sans JP",sans-serif;font-size:11px;font-weight:700}
.apply-art-left{position:absolute;left:30px;top:3240px;width:120px;height:140px;background:rgba(255,255,255,.25);border-radius:8px}
.apply-art-right{position:absolute;left:1000px;top:3200px;width:170px;height:180px;background:rgba(255,255,255,.25);border-radius:8px}

/* footer */
.footer{position:absolute;left:0;top:3400px;width:1200px;height:148px}
.footer-brand{position:absolute;left:40px;top:36px;display:flex;align-items:center;gap:10px;font-weight:700;font-size:18px}
.footer-brand .brand-mark{background:#111}
.footer-links{position:absolute;left:40px;top:96px;display:flex;gap:24px;font-size:11px;color:#555}
.footer-social{position:absolute;left:150px;top:40px;display:none}
.copy{position:absolute;right:40px;top:100px;font-size:10px;color:var(--muted)}
</style>
</head>
<body>

<header class="hero">
  <div class="hero-city" role="img" aria-label="街並みのシルエット"></div>
  <div class="hero-art-left" role="img" aria-label="はしごを運ぶ作業員のイラスト"></div>
  <div class="hero-art-right" role="img" aria-label="家を建てる人々のイラスト"></div>
  <div class="brand"><span class="brand-mark"></span>森野工務店</div>
  <h1 class="hero-title display">EVENT &amp; INFORMATION</h1>
  <div class="hero-rule"></div>
  <p class="hero-sub">イベント＆インフォメーション</p>
</header>
<nav class="social" aria-label="SNS"><span></span><span></span><span></span></nav>
<a class="apply-tab">
  <svg width="28" height="28" viewBox="0 0 28 28"><circle cx="14" cy="14" r="12" fill="none" stroke="#fff" stroke-width="2"/><path d="M8 14l4 4 8-8" fill="none" stroke="#fff" stroke-width="2.5"/></svg>
  <b>APPLY</b><small>お申込み</small>
</a>

<section>
  <div class="events-head center">
    <h2 class="label green display">EVENT</h2>
    <p class="label-ja">最新のイベント情報</p>
  </div>

  <article class="event-card" style="top:740px">
    <div class="event-photo" role="img" aria-label="セミナー会場の写真" style="background:linear-gradient(135deg,#d9c4a8,#8a6a4e)"></div>
    <div class="event-body">
      <h3 class="event-title">セミナープレイス［ミドリノマ］</h3>
      <p class="event-row"><i></i><em>開催日時</em><span>2020年8月7日</span></p>
      <p class="event-row"><i></i><em>開催時間</em><span>10:00〜15:00</span></p>
      <p class="event-row"><i></i><em>会場</em><span>森野工務店</span></p>
    </div>
    <a class="event-apply"><b>APPLY</b><small>お申込み</small></a>
  </article>

  <article class="event-card" style="top:1000px">
    <div class="event-photo" role="img" aria-label="記念イベント会場の建物の写真" style="background:linear-gradient(180deg,#5a88c4,#3c4f6a)"></div>
    <div class="event-body">
      <h3 class="event-title">森野工務店30周年記念イベント・参加者募集！</h3>
      <p class="event-row"><i></i><em>開催日時</em><span>2020年9月7日・2020年9月8日</span></p>
      <p class="event-row"><i></i><em>開催時間</em><span>10:00〜16:00</span></p>
      <p class="event-row"><i></i><em>会場</em><span>森野工務店 第二会場</span></p>
    </div>
    <a class="event-apply"><b>APPLY</b><small>お申込み</small></a>
  </article>

  <article class="event-card" style="top:1260px">
    <div class="event-photo" role="img" aria-label="田園風景の写真" style="background:linear-gradient(180deg,#b8c96a,#7a9a3a)"></div>
    <div class="event-body">
      <h3 class="event-title">自分を知ろう！からだ測定</h3>
      <p class="event-row"><i></i><em>開催日時</em><span>2020年9月17日</span></p>
      <p class="event-row"><i></i><em>開催時間</em><span>10:00〜16:00／13:00〜17:00</span></p>
      <p class="event-row"><i></i><em>会場</em><span>森野公民館 多目的室</span></p>
    </div>
    <a class="event-apply"><b>APPLY</b><small>お申込み</small></a>
  </article>

  <a class="btn btn-more">VIEW MORE</a>
</section>

<section class="news">
  <div class="news-head">
    <h2 class="label display">NEWS</h2>
    <p class="label-ja">お知らせ</p>
  </div>
  <a class="btn news-more">VIEW MORE</a>
  <ul class="news-list">
    <li><time>2020.07.01</time>新築見学会の日程を追加しました。</li>
    <li><time>2020.06.15</time>Webサイトをリニューアルしました。</li>
    <li><time>2020.06.01</time>夏季休業期間のお問い合わせ対応について。</li>
  </ul>
</section>

<section>
  <div class="access-head">
    <h2 class="label display">ACCESS</h2>
    <p class="label-ja">アクセス</p>
  </div>
  <address class="access-addr" style="font-style:normal">〒000-0000　緑野市森野町1-2-3<br>森野工務店 本社ビル1階（駐車場有）</address>
  <div class="map" role="img" aria-label="会社周辺の地図"></div>
  <div class="map-pin">（株）森野工務店</div>
</section>

<section>
  <div class="apply"></div>
  <div class="apply-art-left" role="img" aria-label="切り株のイラスト"></div>
  <div class="apply-art-right" role="img" aria-label="資材を運ぶ人々のイラスト"></div>
  <div class="apply-head center">
    <h2 class="label display">APPLY</h2>
    <p class="label-ja">お申込み</p>
  </div>
  <p class="apply-text">各イベントのお申し込みはこちらからお願いいたします。</p>
  <a class="apply-btn">
    <svg width="22" height="22" viewBox="0 0 22 22"><circle cx="11" cy="11" r="9.5" fill="none" stroke="#f28a1a" stroke-width="2"/><path d="M6.5 11l3 3 6-6" fill="none" stroke="#f28a1a" stroke-width="2.2"/></svg>
    APPLY<small>お申込みフォーム</small>
  </a>
</section>

<footer class="footer">
  <div class="footer-brand"><span class="brand-mark"></span>森野工務店</div>
  <nav class="footer-links"><span>プライバシーポリシー</span><span>サイトマップ</span></nav>
  <p class="copy">Copyright © 森野工務店 All Rights Reserved.</p>
</footer>

</body>
</html>
```